Texas-Based Roofing Company Looking for Creative Billboard Design

We need a billboard designed for a roofing company in the Dallas - Fort Worth area. They are a tech-forward company that uses drone technology to complete roof inspections. We would like to see a design that is out-of-the-box in terms of creativity. It can be marketed towards a hail/wind storm event, or a creative approach to helping customers think of TANNERLY when it comes to roofing needs.

Target Market(s)

residential homeowners

Industry/Entity Type

Roofing

Requirements
Must have
• Creative approach or play on words to elevate brand awareness.

```html
<!DOCTYPE html>
<html lang="en">
<head>
<meta charset="utf-8">
<title>Tannerly Roofing Billboard</title>
<link rel="stylesheet" href="https://fonts.googleapis.com/css2?family=Open+Sans:wght@500&family=Rubik:wght@700&display=swap">
<style>
  :root {
    --stage: #d6d7d9;
    --navy: #213a80;
    --sky: #2aa3df;
    --ocean: #1b6fb0;
    --white: #ffffff;
    --ink: #1c1c1c;
    --gold: #e0a824;
  }
  html, body {
    margin: 0;
    width: 1200px;
    height: 459px;
    overflow: hidden;
    background: var(--stage);
  }
  .billboard {
    position: absolute;
    left: 76px;
    top: 76px;
    width: 1047px;
    height: 306px;
    display: block;
  }
  .brand-name {
    font-family: "Open Sans", sans-serif;
    font-weight: 500;
    fill: var(--ink);
  }
  .tagline {
    font-family: "Open Sans", sans-serif;
    font-weight: 500;
    fill: var(--gold);
  }
  .service {
    font-family: "Rubik", sans-serif;
    font-weight: 700;
    fill: var(--white);
  }
</style>
</head>
<body>
<svg class="billboard" viewBox="0 0 2190 640" xmlns="http://www.w3.org/2000/svg">
  <defs>
    <clipPath id="board-edge"><rect width="2190" height="640"/></clipPath>
    <linearGradient id="swoosh-blue" x1="0" y1="1" x2="1" y2="0">
      <stop offset="0" stop-color="var(--sky)"/>
      <stop offset="0.5" stop-color="#1e8fd0"/>
      <stop offset="1" stop-color="var(--ocean)"/>
    </linearGradient>
    <linearGradient id="ring-blue" x1="0" y1="0" x2="1" y2="1">
      <stop offset="0" stop-color="var(--sky)"/>
      <stop offset="1" stop-color="var(--ocean)"/>
    </linearGradient>
    <linearGradient id="shingle-photo" x1="0" y1="0" x2="0" y2="1">
      <stop offset="0" stop-color="#d3d8de"/>
      <stop offset="0.45" stop-color="#a9a19a"/>
      <stop offset="0.6" stop-color="#7a4a3a"/>
      <stop offset="1" stop-color="#5e3326"/>
    </linearGradient>
    <linearGradient id="tile-photo" x1="0" y1="0" x2="1" y2="1">
      <stop offset="0" stop-color="#d8784a"/>
      <stop offset="0.4" stop-color="#55636f"/>
      <stop offset="0.7" stop-color="#4a5661"/>
      <stop offset="1" stop-color="#d9794a"/>
    </linearGradient>
  </defs>

  <g clip-path="url(#board-edge)">
    <rect class="board-base" width="2190" height="640" fill="var(--white)"/>
    <path class="navy-field" fill="var(--navy)" d="M610,0 H2190 V640 H0 V420 C200,300 420,120 610,0 Z"/>
    <path class="swoosh-band" fill="url(#swoosh-blue)" d="M0,600 C300,470 620,250 1000,95 C1400,-40 1900,-20 2190,140 V180 C1900,30 1400,20 1000,140 C700,260 400,470 60,640 H0 Z"/>
    <path class="headline-field" fill="var(--white)" d="M790,230 C1200,30 1800,-5 2190,160 V460 H790 Z"/>
    <path class="light-stripe" fill="var(--white)" d="M0,585 C230,500 390,410 530,320 L555,345 C420,440 280,560 190,640 H0 Z"/>

    <g class="photo-circle tile-spraying" role="img" aria-label="Photo of a worker spray-painting a terracotta tile roof grey">
      <circle cx="575" cy="322" r="285" fill="url(#ring-blue)"/>
      <circle cx="575" cy="322" r="258" fill="url(#tile-photo)"/>
    </g>
    <g class="photo-circle shingle-install" role="img" aria-label="Photo of a roofer in a safety vest installing shingles">
      <circle cx="170" cy="240" r="225" fill="url(#ring-blue)"/>
      <circle cx="170" cy="240" r="205" fill="url(#shingle-photo)"/>
    </g>
  </g>

  <circle class="brand-dot" cx="1892" cy="190" r="60" fill="var(--gold)"/>
  <text class="brand-name" x="965" y="365" font-size="112" textLength="1105" lengthAdjust="spacingAndGlyphs">TANNERLY ROOFING</text>
  <text class="tagline" x="968" y="422" font-size="38" textLength="1102" lengthAdjust="spacing">BUILDING THE KINGDOM ONE ROOF AT A TIME</text>

  <g class="service-list">
    <g class="bullet" transform="translate(1003,512)">
      <circle r="13" fill="var(--white)"/>
      <path d="M-7,-2.5 H1 V-7 L8,0 L1,7 V2.5 H-7 Z" fill="var(--navy)"/>
    </g>
    <text class="service" x="1027" y="528" font-size="44" textLength="412" lengthAdjust="spacingAndGlyphs">Residential Roofing</text>
    <g class="bullet" transform="translate(1463,512)">
      <circle r="13" fill="var(--white)"/>
      <path d="M-7,-2.5 H1 V-7 L8,0 L1,7 V2.5 H-7 Z" fill="var(--navy)"/>
    </g>
    <text class="service" x="1486" y="528" font-size="44" textLength="428" lengthAdjust="spacingAndGlyphs">Commercial Roofing</text>

    <g class="bullet" transform="translate(815,570)">
      <circle r="13" fill="var(--white)"/>
      <path d="M-7,-2.5 H1 V-7 L8,0 L1,7 V2.5 H-7 Z" fill="var(--navy)"/>
    </g>
    <text class="service" x="837" y="586" font-size="44" textLength="174" lengthAdjust="spacingAndGlyphs">Painting</text>
    <g class="bullet" transform="translate(1031,570)">
      <circle r="13" fill="var(--white)"/>
      <path d="M-7,-2.5 H1 V-7 L8,0 L1,7 V2.5 H-7 Z" fill="var(--navy)"/>
    </g>
    <text class="service" x="1050" y="586" font-size="44" textLength="1065" lengthAdjust="spacingAndGlyphs">Electrical and Concierge VIP Services for Realtors.</text>
  </g>
</svg>
</body>
</html>
```